Website Design for Qolva-iX Software Solutions

Our company (IT) develops (3 main markets):
- Software for selfservice kiosks
- Web- and Mobile applications
- Embedded Software

```html
<!DOCTYPE html>
<html lang="en">
<head>
<meta charset="utf-8">
<title>Qolva-iX Software Solutions</title>
<link rel="stylesheet" href="https://fonts.googleapis.com/css2?family=Roboto:ital,wght@0,400;0,500;1,400&family=Arimo:wght@400;700&display=swap">
<style>
  :root {
    --green-light: #7cc36a;
    --green-mid: #5aa449;
    --green-dark: #3f7a2f;
    --green-text: #2f5a1e;
    --blue-deep: #0f4f78;
    --blue-mid: #1d7aa6;
    --blue-light: #4aa7c9;
    --card-top: #b4e4ee;
    --card-bottom: #2f8cb6;
    --card-title: #1d6a94;
    --card-text: #2e7ea0;
    --panel-fill: rgba(170, 205, 225, 0.82);
    --panel-border: #1b3f5a;
    --ink: #111820;
    --logo: #e07a1f;
    --white: #ffffff;
  }
  * { margin: 0; padding: 0; box-sizing: border-box; }
  html, body { width: 960px; height: 1200px; overflow: hidden; }
  body {
    position: relative;
    font-family: "Arimo", Arial, sans-serif;
    background: linear-gradient(180deg, var(--blue-light) 0%, var(--blue-mid) 40%, var(--blue-deep) 100%);
  }
  .site-header {
    position: absolute; left: 0; top: 0; width: 960px; height: 318px;
    background: linear-gradient(180deg, var(--green-light) 0%, var(--green-mid) 80%, var(--green-dark) 100%);
  }
  .brand {
    position: absolute; left: 32px; top: 10px;
    font-family: "Roboto", sans-serif; font-weight: 500; font-size: 24px;
    letter-spacing: 3px; color: var(--logo);
  }
  .site-title {
    position: absolute; left: 32px; top: 66px;
    font-family: "Roboto", sans-serif; font-weight: 400; font-size: 29px;
    letter-spacing: 1px; color: var(--green-text);
  }
  .intro {
    position: absolute; left: 32px; top: 146px; width: 400px;
    font-size: 12.6px; line-height: 14.4px; color: #1c2a12;
  }
  .hero-art {
    position: absolute; left: 525px; top: 26px; width: 430px; height: 248px;
    border-radius: 20px;
    background: radial-gradient(ellipse at 50% 50%, #cfd8dc 0%, #7fa9c9 45%, rgba(120,180,110,0) 75%);
  }
  .service {
    position: absolute; top: 290px; width: 278px; height: 387px;
    border-radius: 18px 18px 4px 4px;
    background: linear-gradient(180deg, var(--card-top) 0%, #8ccde0 45%, var(--card-bottom) 100%);
    box-shadow: 0 6px 14px rgba(0,0,0,0.45);
  }
  .service--kiosks { left: 23px; }
  .service--apps { left: 336px; }
  .service--embedded { left: 647px; }
  .service__title {
    position: absolute; left: 0; right: 0; top: 14px; text-align: center;
    font-family: "Roboto", sans-serif; font-size: 20px; line-height: 21px;
    color: var(--card-title); text-transform: uppercase;
  }
  .service__icon {
    position: absolute; left: 64px; top: 62px; width: 150px; height: 130px;
    border-radius: 12px;
    background: radial-gradient(circle, #f3d34a 0%, #d6b33a 55%, rgba(150,210,225,0) 75%);
  }
  .service--apps .service__icon { background: radial-gradient(circle, #f1c04a 0%, #3f8fc4 55%, rgba(150,210,225,0) 75%); }
  .service--embedded .service__icon { background: radial-gradient(circle, #eef2f4 0%, #b8c4cc 55%, rgba(150,210,225,0) 75%); }
  .service__text {
    position: absolute; left: 7px; top: 209px; width: 266px;
    font-size: 10.6px; line-height: 14px; color: var(--card-text);
  }
  .button-more {
    position: absolute; left: 50%; top: 340px; width: 115px; height: 25px;
    margin-left: -57px; border-radius: 8px;
    background: linear-gradient(180deg, #d4eef3 0%, #8cc6d6 55%, #5a9fb6 100%);
    border: 1px solid #2f6f88;
    font-size: 9px; line-height: 23px; text-align: center; color: #2e5c6e;
  }
  .news {
    position: absolute; left: 21px; top: 727px; width: 597px; height: 391px;
    background: var(--panel-fill); border: 2px solid var(--panel-border);
  }
  .news__item { position: absolute; left: 10px; width: 575px; }
  .news__item:nth-child(1) { top: 57px; }
  .news__item:nth-child(2) { top: 225px; }
  .news__title {
    font-family: "Roboto", sans-serif; font-style: italic; font-weight: 400;
    font-size: 13px; color: #10253a; letter-spacing: 0.5px; text-transform: uppercase;
    margin-bottom: 4px;
  }
  .news__text { font-size: 10.8px; line-height: 14.5px; color: var(--ink); }
  .news__more { margin-top: 10px; font-size: 10.5px; color: var(--ink); font-style: italic; }
  .news__more span { text-decoration: underline; }
  .certificates {
    position: absolute; left: 645px; top: 726px; width: 280px; height: 229px;
    background: #f2f2f2;
  }
  .social {
    position: absolute; left: 646px; width: 281px; height: 42px;
    border-radius: 10px; border: 1px solid #154a6a;
    background: linear-gradient(180deg, #8fc6dd 0%, #3f8db5 60%, #2a6f98 100%);
    font-family: "Roboto", sans-serif; font-size: 14px; color: var(--ink);
  }
  .social--friends { top: 972px; }
  .social--chirp { top: 1031px; }
  .social__mark {
    position: absolute; left: 14px; top: 8px; width: 26px; height: 26px;
    border-radius: 4px; background: #5f8fb8;
  }
  .social--chirp .social__mark { background: #7fc4e4; }
  .social__label { position: absolute; left: 90px; top: 12px; }
  .site-footer {
    position: absolute; left: 0; top: 1131px; width: 960px; height: 69px;
    border-top: 2px solid #d8e8e0;
    background: linear-gradient(180deg, var(--green-light) 0%, var(--green-mid) 60%, var(--green-dark) 100%);
    text-align: center; font-family: "Roboto", sans-serif; color: var(--ink);
  }
  .footer-nav { margin-top: 7px; font-size: 13px; letter-spacing: 0.3px; }
  .copyright { margin-top: 20px; font-size: 12.5px; }
</style>
</head>
<body>
  <header class="site-header">
    <div class="brand">Qolva-iX</div>
    <h1 class="site-title">QOLVA-IX SOFTWARE SOLUTIONS</h1>
    <p class="intro">Lorem ipsum dolor sit amet, consectetur adipisicing elit, sed do eiusmod tempor incididunt ut labore et dolore magna aliqua. Ut enim ad minim veniam, quis nostrud exercitation ullamco laboris nisi ut aliquip ex ea commodo consequat. Duis aute irure dolor in reprehenderit in voluptate velit esse cillum dolore eu fugiat nulla pariatur. Excepteur sint occaecat cupidatat non proident, sunt in culpa qui officia deserunt mollit anim id est laborum.</p>
    <div class="hero-art" role="img" aria-label="Smartphone surrounded by a burst of colourful app icons"></div>
  </header>

  <section class="service service--kiosks">
    <h2 class="service__title">Kiosks</h2>
    <div class="service__icon" role="img" aria-label="Yellow note with gears and a pencil"></div>
    <p class="service__text">Lorem ipsum dolor sit amet, consectetur adipisicing elit, sed do eiusmod tempor incididunt ut labore et dolore magna aliqua. Ut enim ad minim veniam, quis nostrud exercitation ullamco laboris nisi ut aliquip ex ea commodo consequat. Duis aute irure dolor in reprehenderit in voluptate velit esse cillum dolore eu fugiat nulla pariatur. Excepteur sint occaecat cupidatat non proident, sunt in culpa qui officia deserunt mollit anim id est laborum.</p>
    <div class="button-more">READ MORE</div>
  </section>

  <section class="service service--apps">
    <h2 class="service__title">Web and Mobile<br>Applications</h2>
    <div class="service__icon" role="img" aria-label="Globe beside a yellow folder"></div>
    <p class="service__text">Lorem ipsum dolor sit amet, consectetur adipisicing elit, sed do eiusmod tempor incididunt ut labore et dolore magna aliqua. Ut enim ad minim veniam, quis nostrud exercitation ullamco laboris nisi ut aliquip ex ea commodo consequat. Duis aute irure dolor in reprehenderit in voluptate velit esse cillum dolore eu fugiat nulla pariatur. Excepteur sint occaecat cupidatat non proident, sunt in culpa qui officia deserunt mollit anim id est laborum.</p>
    <div class="button-more">READ MORE</div>
  </section>

  <section class="service service--embedded">
    <h2 class="service__title">Embeded Software</h2>
    <div class="service__icon" role="img" aria-label="Software box with a disc"></div>
    <p class="service__text">Lorem ipsum dolor sit amet, consectetur adipisicing elit, sed do eiusmod tempor incididunt ut labore et dolore magna aliqua. Ut enim ad minim veniam, quis nostrud exercitation ullamco laboris nisi ut aliquip ex ea commodo consequat. Duis aute irure dolor in reprehenderit in voluptate velit esse cillum dolore eu fugiat nulla pariatur. Excepteur sint occaecat cupidatat non proident, sunt in culpa qui officia deserunt mollit anim id est laborum.</p>
    <div class="button-more">READ MORE</div>
  </section>

  <section class="news">
    <article class="news__item">
      <h3 class="news__title">playbetterdaily.nl</h3>
      <p class="news__text">Lorem ipsum dolor sit amet, consectetur adipisicing elit, sed do eiusmod tempor incididunt ut labore et dolore magna aliqua. Ut enim ad minim veniam, quis nostrud exercitation ullamco laboris nisi ut aliquip ex ea commodo consequat. Duis aute irure dolor in reprehenderit in voluptate velit esse cillum dolore eu fugiat nulla pariatur. Excepteur sint occaecat cupidatat non proident, sunt in culpa qui officia deserunt mollit anim id est laborum.</p>
      <p class="news__more"><span>READ MORE</span> &gt;&gt;</p>
    </article>
    <article class="news__item">
      <h3 class="news__title">Le Stade Sports Quiz</h3>
      <p class="news__text">Lorem ipsum dolor sit amet, consectetur adipisicing elit, sed do eiusmod tempor incididunt ut labore et dolore magna aliqua. Ut enim ad minim veniam, quis nostrud exercitation ullamco laboris nisi ut aliquip ex ea commodo consequat. Duis aute irure dolor in reprehenderit in voluptate velit esse cillum dolore eu fugiat nulla pariatur. Excepteur sint occaecat cupidatat non proident, sunt in culpa qui officia deserunt mollit anim id est laborum.</p>
      <p class="news__more"><span>READ MORE</span> &gt;&gt;</p>
    </article>
  </section>

  <aside class="certificates" role="img" aria-label="Area for certificate badges"></aside>

  <div class="social social--friends">
    <span class="social__mark"></span>
    <span class="social__label">Like us on Facepage</span>
  </div>
  <div class="social social--chirp">
    <span class="social__mark"></span>
    <span class="social__label">Follow us at Chirper</span>
  </div>

  <footer class="site-footer">
    <nav class="footer-nav">Home | Discalimer | Site Map | About Us | Contact Us</nav>
    <p class="copyright">All rights reserved @ Qolva-iX 2011-12</p>
  </footer>
</body>
</html>
```